Need a website to promote and sell my book

Using images from the book, I need a website designed that helps promote the book and eventually sell it.
*Need a landing page
*About the author page
*Storefront page to purchase
*Coming soon page
*"Featured in" page that can link to news articles etc.
The images posted here are examples, the winner of the contest will get the images from the finished book. I will provide the exact text to the winner of the contest.

I can also provide images of kids reading the book. For now, I'll just use one, the winner can have them all to choose from.
Updates

Extending deadline to allow for a few more designers to submit and to allow time for me to review and hold a poll

Target Market(s)

Parents, aunts, uncles, grandparents, friends who have kids; teachers, daycare teachers, babysitters etc.

Industry/Entity Type

Custom Publishing

Coding

Coded - Design and coding required

Number of Pages Required

5+ page

Font styles to use
Sans Serif

Colors

Designer to choose colors to be used in the design.

Requirements
Must have
• It must have a fun feel like the book.
Nice to have
• Would be great to have a section that automatically pulls tweets about the book into it.

```html
<!DOCTYPE html>
<html lang="en">
<head>
<meta charset="utf-8">
<title>Marlowe — Featured</title>
<link href="https://fonts.googleapis.com/css2?family=Libre+Baskerville:ital,wght@0,400;0,700;1,400&family=Lato:ital,wght@0,400;0,700;1,400&display=swap" rel="stylesheet">
<style>
:root{
  --accent:#e0553a;
  --ink:#2b2b2b;
  --body:#6a6a6a;
  --muted:#9a9a9a;
  --light:#f5f5f5;
  --cream:#f2f1ed;
  --white:#ffffff;
  --line:#d9d9d9;
  --serif:'Libre Baskerville', Georgia, serif;
  --sans:'Lato', Helvetica, Arial, sans-serif;
}
*{margin:0;padding:0;box-sizing:border-box}
h1,h2,h3{font-weight:400}
html,body{width:1200px;height:2862px;overflow:hidden;background:var(--white)}
body{position:relative;font-family:var(--sans);color:var(--ink)}
.abs{position:absolute}

/* header */
.nav a{position:absolute;top:58px;font-family:var(--serif);font-size:12px;letter-spacing:1px;color:var(--ink);text-decoration:none;text-transform:uppercase}
.nav a.underline{text-decoration:underline;text-underline-offset:3px}
.nav a.active{color:var(--accent);text-decoration:underline;text-underline-offset:3px}
.brand{position:absolute;left:470px;top:38px;width:190px;text-align:center}
.brand-name{font-family:var(--serif);font-size:24px;letter-spacing:3px;border-bottom:1px solid var(--line);padding-bottom:4px}
.brand-tag{font-family:var(--serif);font-size:8px;letter-spacing:1px;color:var(--muted);margin-top:4px}

/* page hero */
.page-hero{left:0;top:130px;width:1200px;height:226px;background:linear-gradient(90deg,#e4e1dd,#ece9e6 40%,#e2dfdc)}
.page-title{left:159px;top:224px;font-family:var(--serif);font-size:32px;letter-spacing:1px}
.crumbs{right:164px;top:235px;font-family:var(--serif);font-style:italic;font-size:16px}
.crumbs span{color:var(--accent)}

/* featured */
.eyebrow{font-family:var(--serif);font-size:14px;letter-spacing:.5px;color:var(--accent);text-transform:uppercase}
.feat-title{left:161px;top:470px;font-family:var(--serif);font-size:40px;line-height:46px;width:400px}
.feat-copy{left:161px;top:578px;width:360px;font-size:12px;line-height:22.5px;color:var(--body)}
.tag{left:161px;top:676px;font-family:var(--serif);font-size:9px;color:var(--muted);letter-spacing:.5px}
.price{left:161px;top:713px;font-family:var(--serif);font-size:26px;color:var(--accent)}
.btn{position:absolute;height:45px;display:flex;align-items:center;justify-content:center;gap:8px;font-size:11px;font-weight:700;text-transform:uppercase;letter-spacing:.3px}
.btn-solid{background:var(--accent);color:var(--white)}
.btn-outline{border:2px solid var(--accent);color:var(--accent);background:var(--white)}
.cover{position:absolute}

/* reviews */
.reviews{left:0;top:889px;width:1200px;height:939px;background:var(--light)}
.center{left:0;width:1200px;text-align:center}
.section-title{font-family:var(--serif);font-size:38px}
.review-img{position:absolute;width:202px;height:240px;background:linear-gradient(160deg,#8fc6e0,#b9d9e6 55%,#e8c88a)}
.review{position:absolute;width:210px;height:250px}
.review h3{font-family:var(--serif);font-size:15.5px;line-height:30px;white-space:nowrap}
.review .by{font-style:italic;font-size:12px;color:var(--body);margin-top:10px}
.review p{font-size:12px;line-height:22.5px;color:var(--body);margin-top:12px}
.review .more{position:absolute;left:0;top:234px;font-size:11.5px;font-weight:700;color:var(--accent)}

/* testimonial */
.testimonial{left:0;top:1828px;width:1200px;height:566px;background:var(--cream)}
.quote{font-family:var(--serif);font-style:italic;font-size:22px;line-height:44px}
.circle{position:absolute;width:52px;height:52px;border-radius:50%;display:flex;align-items:center;justify-content:center}

/* newsletter */
.news-card{left:163px;top:2472px;width:874px;height:317px;background:var(--white);box-shadow:0 1px 8px rgba(0,0,0,.12)}
</style>
</head>
<body>

<header class="nav">
  <a style="left:159px">Home</a>
  <a style="left:231px">About</a>
  <a class="underline" style="left:309px">Storefront</a>
  <a style="left:737px">Coming Soon</a>
  <a class="active" style="left:869px">Featured</a>
  <a style="left:973px">Contact</a>
  <div class="brand">
    <div class="brand-name">MARLOWE</div>
    <div class="brand-tag">AUTHOR &amp; WRITER</div>
  </div>
</header>

<div class="abs page-hero" role="img" aria-label="Faded photo of a bookshop café interior"></div>
<h1 class="abs page-title">Featured</h1>
<div class="abs crumbs">Home / <span>Featured</span></div>

<!-- featured book -->
<div class="abs eyebrow" style="left:165px;top:428px">Featured Books</div>
<h2 class="abs feat-title">Lorem Ipsatui Of Any Dolor</h2>
<p class="abs feat-copy">Lorem ipsum dolor sit amet, consectetu eradipiscing elit. Aenean commodo ligula eget dolor. Simply. Aenean massa. Cum sociis natoque penatibus et magnis Lorem ipsum dolor sit amet, consec-teuter adipiscing elit. Cum sociisnatoque penatibus et ait</p>
<div class="abs tag">FOR KIDS</div>
<div class="abs price">$15.00</div>
<svg class="abs" style="left:385px;top:711px" width="54" height="16" viewBox="0 0 54 16">
  <path d="M18 8H2M8 2L2 8l6 6" fill="none" stroke="#e9c3b9" stroke-width="2"/>
  <path d="M34 8h18M46 2l6 6-6 6" fill="none" stroke="#e0553a" stroke-width="2.4"/>
</svg>
<div class="btn btn-solid" style="left:161px;top:770px;width:129px">Quick View</div>
<div class="btn btn-outline" style="left:313px;top:770px;width:128px">Add to cart
  <svg width="12" height="11" viewBox="0 0 12 11"><path d="M0 1h2l2 6h6l1.5-4.5H3" fill="none" stroke="#e0553a" stroke-width="1.3"/><circle cx="5" cy="9.5" r="1" fill="#e0553a"/><circle cx="9" cy="9.5" r="1" fill="#e0553a"/></svg>
</div>

<div class="cover" style="left:578px;top:490px;width:190px;height:300px;background:linear-gradient(165deg,#7fbfdf,#a8d3e6 55%,#e9c585);transform:skewY(4deg);box-shadow:10px 12px 18px rgba(0,0,0,.18)" role="img" aria-label="Featured children's chemistry book cover, standing in 3D"></div>
<div class="cover" style="left:829px;top:552px;width:95px;height:122px;background:linear-gradient(#4c3b3b,#3a2e2e);box-shadow:3px 3px 6px rgba(0,0,0,.2)" role="img" aria-label="Dark brown classic short stories book cover"></div>
<div class="cover" style="left:942px;top:552px;width:96px;height:122px;background:linear-gradient(#2e5f6e,#24505c);box-shadow:3px 3px 6px rgba(0,0,0,.2)" role="img" aria-label="Teal novel cover with bold coloured title"></div>

<!-- reviews -->
<section class="abs reviews"></section>
<div class="abs center eyebrow" style="top:962px">Book Reviews</div>
<h2 class="abs center section-title" style="top:1003px">Latest Reviews Of The Book</h2>

<div class="review-img" style="left:161px;top:1106px" role="img" aria-label="Children's chemistry book cover"></div>
<div class="review" style="left:386px;top:1100px"><h3>What Simply Dummy Of<br>Text Is A Lorem Ipsum</h3><div class="by">By: LOREM IPSUM</div><p>Lorem ipsum dolor sit amet, consecte-tu eradipiscing elit. Aenean commodo ligula eget dolor. Simply. Aenean atn massa. Cum sociis natoque penatibus if any lorem ipsum is dolor</p><span class="more">READ THE REVIEW &gt;&gt;</span></div>

<div class="review-img" style="left:611px;top:1106px" role="img" aria-label="Children's chemistry book cover"></div>
<div class="review" style="left:836px;top:1100px"><h3>What Simply Dummy Of<br>Text Is A Lorem Ipsum</h3><div class="by">By: LOREM IPSUM</div><p>Lorem ipsum dolor sit amet, consecte-tu eradipiscing elit. Aenean commodo ligula eget dolor. Simply. Aenean atn massa. Cum sociis natoque penatibus if any lorem ipsum is dolor</p><span class="more">READ THE REVIEW &gt;&gt;</span></div>

<div class="review-img" style="left:161px;top:1369px" role="img" aria-label="Children's chemistry book cover"></div>
<div class="review" style="left:386px;top:1363px"><h3>What Simply Dummy Of<br>Text Is A Lorem Ipsum</h3><div class="by">By: LOREM IPSUM</div><p>Lorem ipsum dolor sit amet, consecte-tu eradipiscing elit. Aenean commodo ligula eget dolor. Simply. Aenean atn massa. Cum sociis natoque penatibus if any lorem ipsum is dolor</p><span class="more">READ THE REVIEW &gt;&gt;</span></div>

<div class="review-img" style="left:611px;top:1369px" role="img" aria-label="Children's chemistry book cover"></div>
<div class="review" style="left:836px;top:1363px"><h3>What Simply Dummy Of<br>Text Is A Lorem Ipsum</h3><div class="by">By: LOREM IPSUM</div><p>Lorem ipsum dolor sit amet, consecte-tu eradipiscing elit. Aenean commodo ligula eget dolor. Simply. Aenean atn massa. Cum sociis natoque penatibus if any lorem ipsum is dolor</p><span class="more">READ THE REVIEW &gt;&gt;</span></div>

<div class="btn btn-solid" style="left:535px;top:1669px;width:129px">View All</div>

<!-- testimonial -->
<section class="abs testimonial"></section>
<svg class="abs" style="left:576px;top:1980px" width="48" height="38" viewBox="0 0 48 38">
  <circle cx="11" cy="11" r="10" fill="#e0553a"/><path d="M19 14c0 12-7 20-16 22l-1-3c6-3 9-8 9-14z" fill="#e0553a"/>
  <circle cx="35" cy="11" r="10" fill="#e0553a"/><path d="M43 14c0 12-7 20-16 22l-1-3c6-3 9-8 9-14z" fill="#e0553a"/>
</svg>
<div class="abs center quote" style="top:2066px">Lamps wayfarers stumptown, intelligentsia butcher pok<br>pok lomo meditation kitsch food truck tumeric salvia</div>
<div class="abs center" style="top:2202px;font-family:var(--serif);font-size:16px">CORINNE WELLS</div>
<div class="abs center" style="top:2230px;font-family:var(--serif);font-style:italic;font-size:12px;color:var(--body)">Reporter/Publisher</div>
<div class="circle" style="left:161px;top:2087px;border:2px solid #e3e1dc">
  <svg width="10" height="14" viewBox="0 0 10 14"><path d="M8 1L2 7l6 6" fill="none" stroke="#d7d4cf" stroke-width="1.5"/></svg>
</div>
<div class="circle" style="left:987px;top:2087px;background:var(--white)">
  <svg width="10" height="14" viewBox="0 0 10 14"><path d="M2 1l6 6-6 6" fill="none" stroke="#e0553a" stroke-width="1.5"/></svg>
</div>

<!-- newsletter -->
<div class="abs" style="left:820px;top:2394px;width:380px;height:90px;background:linear-gradient(90deg,rgba(255,255,255,0),#f3ece4 50%,#dfe6cf)" role="img" aria-label="Faint desk scene with notebook, pen and plant"></div>
<div class="abs news-card"></div>
<h2 class="abs section-title" style="left:200px;top:2540px;width:450px;text-align:center">Join The Newsletter</h2>
<div class="abs" style="left:200px;top:2594px;width:450px;text-align:center;font-family:var(--serif);font-size:11px;color:var(--muted)">Subscribe To Get In Touch</div>
<div class="abs" style="left:236px;top:2690px;width:375px;border-bottom:1px solid #bdbdbd;height:25px">
  <div style="text-align:center;font-family:var(--serif);font-size:14px;color:var(--muted)">Enter Your E-mail</div>
  <svg style="position:absolute;right:0;top:4px" width="14" height="10" viewBox="0 0 14 10"><path d="M0 5h12M8 1l4 4-4 4" fill="none" stroke="#777" stroke-width="1.2"/></svg>
</div>
<div class="cover" style="left:765px;top:2550px;width:200px;height:150px;background:linear-gradient(150deg,#3a9aa6,#2b7f8c 60%,#e7e7e7);clip-path:polygon(10% 0,60% 5%,100% 55%,100% 88%,55% 100%,0 85%)" role="img" aria-label="Stack of teal business books"></div>

</body>
</html>
```